Bday & 7th year in Singapore

I'll be celebrating my thirty something birthday and 7th year in Singapore on Sat 29 June 2013, 830pm til late. Still looking for a venue so please leave some space for it and the address so it can be added.
Required:
Sat, 29 June
830pm
Venue TBC
I would like the poster to have an "infographic" look and feel, ideally with blue, grey, and red tones.
I would like invitees to feel that it's going to a great night of live music, drinks and mingling with existing and new friends so it would be awesome if they can be there.
I love traveling, clubbing, going on food adventures, singing.
People need to know that it's primarily a bday party (main design element) but that I'm also celebrating my 7th year in Singapore.
I'm looking for the most creative design so people will get excited and book their diaries as soon as they see the invitation.
Output required: high quality JPEG I can post on Chatterloop event page and also something I can use for A3 printing. Winning designer should be able to accommodate a revision on venue after decision is made as I can only confirm venue after the deadline.
Updates
Reason: Extended the deadline as I realise 2 days is quite tight given nature of the project.
Reason: Waiting for venue to be confirmed so it can be built into the poster
Target Market(s)
Invitees would be between 23 and 35 years old so should appeal to them
Industry/Entity Type
Printing
Requirements
Must have
- Singapore famous landmarks like Corvane Quay Towers, Singapore skyline, Vellmont Hall, Brisktail, but they should not be the centre of attraction
Nice to have
- My photo (attached) but drawn in a nice way

```html
<!DOCTYPE html>
<html lang="en">
<head>
<meta charset="utf-8">
<title>Thirty-something Birthday &amp; Seventh Year in Singapore</title>
<link rel="stylesheet" href="https://fonts.googleapis.com/css2?family=Nunito:wght@700;800;900&display=swap">
<style>
:root{
  --sky:#5fb2c9;
  --sky-deep:#3f93ad;
  --flame:#e0502c;
  --maroon:#5b2424;
  --cream:#f8dfa6;
  --ink:#4a1d1d;
  --blue:#3d9ec0;
  --sun:#f2c02e;
  --peach:#f7c79a;
  --pink:#f3b7c9;
  --cyan:#7fc6df;
  --lemon:#f7ea2a;
}
*{margin:0;padding:0;box-sizing:border-box}
html,body{width:1200px;height:2452px;overflow:hidden;background:var(--sky)}
body{font-family:"Nunito",Arial,sans-serif;font-weight:900;color:var(--cream)}
.poster{position:relative;width:1200px;height:2452px;background:radial-gradient(circle at 30% 20%,var(--sky),var(--sky-deep) 140%)}
.frame{position:absolute;left:48px;top:48px;width:1104px;height:2356px;background:var(--flame)}
.field{position:absolute;left:88px;top:88px;width:1024px;height:2276px;background:var(--maroon)}
.abs{position:absolute}
.age{left:186px;top:150px;font-size:250px;line-height:1;color:var(--cream);letter-spacing:-6px}
.birth{left:192px;top:410px;font-size:100px;line-height:1;color:var(--flame)}
.day{left:192px;top:530px;font-size:122px;line-height:1;color:var(--blue)}
.portraits{left:560px;top:160px;width:500px;height:700px;display:grid;grid-template-columns:1fr 1fr;grid-template-rows:1fr 1fr;gap:12px}
.cake{left:192px;top:680px;width:328px;height:400px;background:linear-gradient(180deg,var(--maroon) 0 34%,var(--sun) 34% 56%,var(--blue) 56% 78%,var(--flame) 78% 100%)}
.date-card{left:728px;top:900px;width:320px;height:500px;background:var(--cream);color:var(--ink);text-align:center;padding-top:30px}
.date-card .pointer{position:absolute;left:-60px;top:120px}
.date-card .sat{font-size:76px;line-height:1}
.date-card .num{font-size:110px;line-height:1;color:var(--flame)}
.date-card .month{font-size:76px;line-height:1}
.date-card .time{font-size:54px;line-height:1.1;color:var(--flame)}
.date-card .venue{font-size:58px;line-height:1}
.ribbon{position:absolute}
.ribbon svg{position:absolute;left:0;top:0}
.ribbon span{position:absolute;left:0;right:0;text-align:center;font-size:72px;line-height:1}
.love-card{left:168px;top:1640px;width:312px;height:580px;background:var(--blue);color:var(--ink)}
.love-card .pointer{position:absolute;left:116px;top:-60px}
.love-card .i{position:absolute;left:64px;top:10px;font-size:90px;line-height:1;color:var(--cream)}
.love-card .love{position:absolute;left:34px;top:100px;font-size:80px;line-height:1;color:var(--flame)}
.love-card .item{position:absolute;line-height:1}
.icon{position:absolute}
.night-card{left:620px;top:1680px;width:428px;height:560px;background:var(--cream);color:var(--ink)}
.night-card .pointer{position:absolute;left:24px;top:-60px}
.night-card .great{position:absolute;right:24px;top:24px;text-align:right;font-size:52px;line-height:1.05;color:var(--flame)}
.night-card .music{position:absolute;right:24px;top:160px;font-size:58px;line-height:1;color:var(--blue)}
.night-card .drinks{position:absolute;left:24px;top:280px;font-size:56px;line-height:1;color:var(--blue)}
.night-card .mingle{position:absolute;right:24px;top:420px;font-size:30px;line-height:1.05;text-align:right}
.footer{left:88px;width:1024px;top:2296px;text-align:center;font-size:42px;line-height:1;color:var(--cream)}
.footer em{font-style:normal;color:var(--flame)}
</style>
</head>
<body>
<main class="poster">
  <div class="frame"></div>
  <div class="field"></div>

  <div class="abs age">3?</div>
  <div class="abs birth">BIRTH</div>
  <div class="abs day">DAY</div>

  <div class="abs portraits" role="img" aria-label="Four-panel pop-art portrait of the host in tinted colours">
    <div style="background:var(--cyan)"></div>
    <div style="background:var(--peach)"></div>
    <div style="background:var(--pink)"></div>
    <div style="background:var(--lemon)"></div>
  </div>

  <div class="abs cake" role="img" aria-label="Birthday cake with candles and zigzag layers in yellow, blue and red"></div>

  <div class="abs date-card">
    <svg class="pointer" width="64" height="90" viewBox="0 0 64 90"><polygon points="64,0 0,45 64,90" fill="#f8dfa6"/></svg>
    <div class="sat">SAT</div>
    <div class="num">29</div>
    <div class="month">JUNE</div>
    <div class="time">830PM</div>
    <div class="venue">VENUE<br>TBC</div>
  </div>

  <div class="ribbon" style="left:160px;top:1160px;width:520px;height:120px">
    <svg width="520" height="120" viewBox="0 0 520 120"><polygon points="0,10 520,0 490,60 520,120 0,110 30,60" fill="#f8dfa6"/></svg>
    <span style="top:24px;color:var(--ink)">SEVENTH</span>
  </div>
  <div class="ribbon" style="left:300px;top:1300px;width:420px;height:120px">
    <svg width="420" height="120" viewBox="0 0 420 120"><polygon points="0,0 420,10 390,60 420,110 0,120 30,60" fill="#e0502c"/></svg>
    <span style="top:24px;color:var(--cream)">YEAR IN</span>
  </div>
  <div class="ribbon" style="left:240px;top:1450px;width:600px;height:140px">
    <svg width="600" height="140" viewBox="0 0 600 140"><polygon points="0,15 600,0 570,70 600,140 0,125 30,70" fill="#f8dfa6"/></svg>
    <span style="top:34px;color:var(--ink)">SINGAPORE</span>
  </div>

  <div class="abs love-card">
    <svg class="pointer" width="80" height="64" viewBox="0 0 80 64"><polygon points="0,64 40,0 80,64" fill="#3d9ec0"/></svg>
    <div class="i">I</div>
    <div class="love">l♥ve</div>
    <div class="icon" role="img" aria-label="Traveller icon" style="left:210px;top:196px;width:60px;height:60px;background:var(--sun)"></div>
    <div class="item" style="left:24px;top:272px;font-size:34px;color:var(--flame)">travelling</div>
    <div class="icon" role="img" aria-label="Club icon" style="left:30px;top:324px;width:50px;height:50px;background:var(--flame)"></div>
    <div class="item" style="left:92px;top:326px;font-size:44px">ing</div>
    <div class="item" style="left:24px;top:396px;font-size:26px;line-height:1.1">going<br>on food<br>adventures</div>
    <div class="icon" role="img" aria-label="Globe icon" style="left:214px;top:404px;width:60px;height:60px;background:var(--cream);border-radius:50%"></div>
    <div class="icon" role="img" aria-label="Singer icon" style="left:24px;top:500px;width:40px;height:50px;background:var(--flame)"></div>
    <div class="item" style="left:76px;top:506px;font-size:40px">singing</div>
  </div>

  <div class="abs night-card">
    <svg class="pointer" width="80" height="64" viewBox="0 0 80 64"><polygon points="0,64 40,0 80,64" fill="#f8dfa6"/></svg>
    <div class="icon" role="img" aria-label="Guitar illustration" style="left:24px;top:24px;width:90px;height:126px;background:var(--blue)"></div>
    <div class="great">GREAT<br>NIGHT OF</div>
    <div class="music">live music</div>
    <div class="drinks">drinks</div>
    <div class="icon" role="img" aria-label="Cocktail glass and drinks illustration" style="right:24px;top:250px;width:110px;height:140px;background:var(--blue)"></div>
    <div class="icon" role="img" aria-label="Silhouettes of friends mingling" style="left:24px;top:400px;width:120px;height:130px;background:var(--blue)"></div>
    <div class="mingle">mingling<br>with existing<br>&amp; NEW FRIENDS</div>
  </div>

  <div class="abs footer">so it would be <em>AWESOME</em> if <em>U</em> can <em>BE THERE!</em></div>
</main>
</body>
</html>
```